Pet CBD Brand needs a new packaging design*

Dear Designers,<br/><br/>Our brand develops CBD products for animals (dogs & cats) for french speaking customers.<br/><br/>We already have an existing packaging design (see attached files) but would like to freshen the design. The final design should communicate safety & modernity. The design should also clearly express this is a product destined for pets.<br/><br/>We are looking for someone who could redesign the labels of our product line, which includes the following 2 products:<br/>- CBD snacks (250 ml clear jar) label size: 220 x 58 mm<br/>- CBD spray (30 ml clear bottle) label + packaging box.<br/><br/>Please find some important additional aspects:<br/>- We would like to keep our green colors which match our corporate identity (please Google us & visit our website to get a feel for our identity)<br/>**Dark Green RGB(53, 153, 128)<br/>** Light Green RGB(231, 236, 232)<br/><br/>Technical instructions from our printing partner:<br/>- Format: .PDF<br/>- Margins: 2,5 mm<br/>- Colors : CMYK<br/>- All text must be vectorized<br/>- Printing standard: ISOcoated V2<br/>- Minimum resolutions: 300 dpi for images, 1,200 dpi for graphics
Target Market(s)
Pet owners, CBD shops, veterinary clinics
Industry/Entity Type
Alternative Medicine

```html
<!DOCTYPE html>
<html lang="fr">
<head>
<meta charset="utf-8">
<title>Verdalis – étiquettes CBD pour animaux</title>
<link rel="stylesheet" href="https://fonts.googleapis.com/css2?family=Montserrat:wght@400;500;600;700&family=Roboto+Slab:wght@700&display=swap">
<style>
  :root {
    --green: #359980;
    --green-soft: #3da286;
    --ink: #1c2f24;
    --grey: #45504a;
    --paper: #ffffff;
    --backdrop: #e7ece8;
  }
  * { box-sizing: border-box; margin: 0; padding: 0; }
  html, body { width: 1200px; height: 852px; overflow: hidden; }
  body {
    background: var(--backdrop);
    font-family: "Montserrat", sans-serif;
    color: var(--grey);
    position: relative;
  }
  .label {
    position: absolute;
    background: var(--paper);
    overflow: hidden;
  }
  .top-curve { position: absolute; top: 0; left: 0; width: 100%; display: block; }
  .paw-band {
    position: absolute; left: 0; bottom: 0; width: 100%;
    background: var(--green);
  }
  .range-name {
    position: absolute;
    transform-origin: left top;
    transform: rotate(-90deg);
    color: var(--green);
    font-weight: 400;
    white-space: nowrap;
  }
  .brand {
    position: absolute;
    font-family: "Roboto Slab", serif;
    font-weight: 700;
    color: var(--ink);
    display: flex; align-items: center;
  }
  .brand-dot {
    display: inline-block; border-radius: 50%; background: var(--green);
  }
  .animals {
    position: absolute;
    color: var(--green);
    font-weight: 500;
    line-height: 1.15;
  }
  .art { position: absolute; background: var(--green); border-radius: 6px; opacity: .9; }
  .rule { position: absolute; height: 1.5px; background: var(--green); }
  .product {
    position: absolute; color: var(--green); font-weight: 700;
    text-align: center; line-height: 1.3;
  }
  .specs {
    position: absolute; display: flex; justify-content: space-between;
    color: var(--green); font-weight: 400; letter-spacing: 2px;
  }

  /* jar label */
  .jar { left: 40px; top: 230px; width: 560px; height: 400px; }
  .jar .top-curve { height: 50px; }
  .jar .paw-band { height: 82px; }
  .jar .range-name { left: 20px; top: 300px; font-size: 20px; letter-spacing: 8px; }
  .jar .brand { left: 70px; top: 108px; font-size: 34px; gap: 10px; }
  .jar .brand-dot { width: 14px; height: 14px; }
  .jar .animals { left: 70px; top: 178px; font-size: 16px; }
  .jar .art { left: 205px; top: 165px; width: 55px; height: 42px; }
  .jar .rule-a { left: 70px; top: 218px; width: 195px; }
  .jar .product { left: 62px; top: 229px; width: 210px; font-size: 16px; letter-spacing: 4px; }
  .jar .rule-b { left: 70px; top: 262px; width: 195px; }
  .jar .specs { left: 70px; top: 275px; width: 195px; font-size: 15px; }
  .jar .notes {
    position: absolute; left: 320px; top: 52px; width: 215px;
    font-size: 11.5px; line-height: 1.35; color: var(--grey);
  }
  .jar .notes h3 { color: var(--green); font-size: 12px; font-weight: 700; margin-top: 12px; }

  /* box front */
  .box { left: 625px; top: 45px; width: 285px; height: 740px; }
  .box .top-curve { height: 80px; }
  .box .paw-band { height: 92px; }
  .box .range-name { left: 48px; top: 592px; font-size: 28px; letter-spacing: 12px; }
  .box .brand { left: 48px; top: 198px; width: 210px; justify-content: center; font-size: 34px; gap: 10px; }
  .box .brand-dot { width: 14px; height: 14px; }
  .box .art { left: 110px; top: 300px; width: 140px; height: 80px; }
  .box .animals { left: 100px; top: 408px; width: 160px; text-align: center; font-size: 19px; }
  .box .rule-a { left: 102px; top: 488px; width: 145px; }
  .box .product { left: 95px; top: 510px; width: 160px; font-size: 27px; letter-spacing: 7px; }
  .box .rule-b { left: 102px; top: 598px; width: 145px; }
  .box .specs { left: 102px; top: 623px; width: 150px; font-size: 13px; }

  /* bottle label */
  .bottle { left: 935px; top: 330px; width: 225px; height: 330px; }
  .bottle .top-curve { height: 60px; }
  .bottle .paw-band { height: 68px; }
  .bottle .range-name { left: 22px; top: 252px; font-size: 15px; letter-spacing: 6px; }
  .bottle .brand { left: 55px; top: 92px; font-size: 20px; gap: 6px; }
  .bottle .brand-dot { width: 9px; height: 9px; }
  .bottle .animals { left: 60px; top: 150px; font-size: 11.5px; }
  .bottle .art { left: 150px; top: 148px; width: 48px; height: 30px; }
  .bottle .rule-a { left: 60px; top: 186px; width: 138px; }
  .bottle .product { left: 55px; top: 193px; width: 148px; font-size: 14px; letter-spacing: 3.5px; }
  .bottle .rule-b { left: 60px; top: 222px; width: 138px; }
  .bottle .specs { left: 60px; top: 230px; width: 138px; font-size: 9.5px; letter-spacing: 1px; }
</style>
</head>
<body>

<section class="label jar" aria-label="Étiquette du pot de friandises">
  <svg class="top-curve" viewBox="0 0 560 50" preserveAspectRatio="none" aria-hidden="true">
    <path d="M0 0H560V10H340Q285 10 280 48Q275 10 220 10H0Z" fill="var(--green)"/>
  </svg>
  <div class="range-name">VERDAFRIAND</div>
  <div class="brand"><span class="brand-dot"></span>VERDALIS</div>
  <div class="animals">POUR CHIENS</div>
  <div class="art" role="img" aria-label="Silhouette d'un chien"></div>
  <div class="rule rule-a"></div>
  <div class="product">FRIANDISES CBD</div>
  <div class="rule rule-b"></div>
  <div class="specs"><span>250g</span><span>0% THC</span></div>
  <div class="notes">
    <p>Soucieux du bien-être de votre compagnon ? Ces encas aux ingrédients sains le récompensent à tout moment.</p>
    <h3>Stockage</h3>
    <p>Conserver à l'abri de la chaleur, hors de portée des enfants.</p>
    <h3>Avertissement</h3>
    <p>Produit destiné aux animaux de compagnie. Demandez conseil à votre vétérinaire.</p>
  </div>
  <div class="paw-band" role="img" aria-label="Bande verte à motif d'empreintes de pattes"></div>
</section>

<section class="label box" aria-label="Face avant de l'étui du spray">
  <svg class="top-curve" viewBox="0 0 285 80" preserveAspectRatio="none" aria-hidden="true">
    <path d="M0 0H285V8H190Q150 8 143 78Q136 8 95 8H0Z" fill="var(--green)"/>
  </svg>
  <div class="range-name">VERDACALIN</div>
  <div class="brand"><span class="brand-dot"></span>VERDALIS</div>
  <div class="art" role="img" aria-label="Silhouettes d'un chat et d'un chien"></div>
  <div class="animals">POUR CHIENS<br>&amp; CHATS</div>
  <div class="rule rule-a"></div>
  <div class="product">SPRAY<br>CBD</div>
  <div class="rule rule-b"></div>
  <div class="specs"><span>30ML</span><span>0% THC</span></div>
  <div class="paw-band" role="img" aria-label="Bande verte à motif d'empreintes de pattes"></div>
</section>

<section class="label bottle" aria-label="Étiquette du flacon spray">
  <svg class="top-curve" viewBox="0 0 225 60" preserveAspectRatio="none" aria-hidden="true">
    <path d="M0 0H225V8H150Q120 8 113 58Q106 8 75 8H0Z" fill="var(--green)"/>
  </svg>
  <div class="range-name">VERDACALIN</div>
  <div class="brand"><span class="brand-dot"></span>VERDALIS</div>
  <div class="animals">POUR CHIENS<br>&amp; CHATS</div>
  <div class="art" role="img" aria-label="Silhouettes d'un chat et d'un chien"></div>
  <div class="rule rule-a"></div>
  <div class="product">SPRAY CBD</div>
  <div class="rule rule-b"></div>
  <div class="specs"><span>30ML</span><span>0% THC</span></div>
  <div class="paw-band" role="img" aria-label="Bande verte à motif d'empreintes de pattes"></div>
</section>

</body>
</html>
```